Designing the poster for an original Broadway-style musical

We need a poster design for the original children's musical, MOSS PETAL AND THE JUMPING GNOMES. The had avery successful run and it is now being published. This poster/graphic design will be used for the publication cover as well as the poster for future productions. The design needs to incorporate the title: MOSS PETAL AND THE JUMPING GNOMES. It must also include: Book by Tod Varga, Music by Ulric Penhall, and Lyrics by Marisol Varga. It should be a Broadway caliber design.

Target Market(s)

Theatre Producers, Theatre audiences

Industry/Entity Type

Entertainment

Requirements
Must have
• MOSS PETAL AND THE JUMPING GNOMES
• Book by Tod Varga, Music by Ulric Penhall, Lyrics by Marisol Varga
Nice to have
• Colorful, bright, energetic.
Should not have
• No Halvern figures. As seen in our photos... our Moss Petal resembles Halvern's but is our own.

```html
<!DOCTYPE html>
<html lang="en">
<head>
<meta charset="utf-8">
<title>Moss Petal and the Jumping Gnomes — Musical Poster</title>
<link rel="stylesheet" href="https://fonts.googleapis.com/css2?family=Cinzel:wght@500&family=Cormorant+Garamond:wght@600;700&family=Almendra:wght@400&display=swap">
<style>
  :root {
    --page: #ffffff;
    --night: #050507;
    --fog: #4a4a5a;
    --moss: #3d5a1c;
    --glow-green: rgba(120, 190, 40, 0.55);
    --glow-violet: rgba(170, 40, 170, 0.6);
    --glow-teal: rgba(30, 150, 170, 0.55);
    --title-fill: #e6f3d6;
    --title-edge: #d9546a;
    --ink-light: #f4f4f4;
  }
  * { margin: 0; padding: 0; box-sizing: border-box; }
  html, body {
    width: 1200px; height: 1200px; overflow: hidden;
    background: var(--page);
  }
  .poster {
    position: absolute;
    left: 214px; top: 54px;
    width: 771px; height: 1091px;
    overflow: hidden;
    background: var(--night);
  }
  .poster-art {
    position: absolute; inset: 0;
    background:
      radial-gradient(ellipse 55% 9% at 45% 44%, var(--glow-violet), transparent 70%),
      radial-gradient(ellipse 45% 8% at 70% 53%, var(--glow-violet), transparent 70%),
      radial-gradient(ellipse 40% 10% at 40% 64%, var(--glow-teal), transparent 70%),
      radial-gradient(ellipse 40% 10% at 60% 38%, var(--glow-green), transparent 70%),
      radial-gradient(ellipse 50% 10% at 65% 72%, var(--glow-green), transparent 70%),
      linear-gradient(to bottom, transparent 84%, var(--moss) 92%, #1c2a0c 100%),
      linear-gradient(to bottom, var(--fog) 0%, #2c2c36 22%, #0d0d12 50%, var(--night) 80%);
  }
  .poster-label {
    position: absolute; top: 118px; left: 0; right: 0;
    text-align: center;
    font-family: "Cinzel", serif;
    font-size: 38px; letter-spacing: 1px;
    color: var(--ink-light);
  }
  .poster-title {
    position: absolute; top: 240px; left: 0; right: 0;
    text-align: center;
    font-family: "Cormorant Garamond", serif;
    font-weight: 700;
    color: var(--title-fill);
    -webkit-text-stroke: 1px var(--title-edge);
    text-shadow: 0 0 12px rgba(220, 255, 200, 0.35);
  }
  .poster-title span { display: block; line-height: 1; }
  .title-main { font-size: 100px; margin-bottom: 30px; }
  .title-small { font-size: 100px; margin-bottom: 24px; }
  .title-big { font-size: 104px; margin-bottom: 24px; }
  .poster-credits {
    position: absolute; top: 1028px; left: 0; right: 0;
    text-align: center;
    font-family: "Almendra", serif;
    font-size: 22px; line-height: 28px;
    color: var(--ink-light);
  }
</style>
</head>
<body>
  <main class="poster">
    <div class="poster-art" role="img" aria-label="Misty night forest with a lit cabin among dark trees, bands of green, violet and teal sparkles, and grass along the bottom"></div>
    <p class="poster-label">MUSICAL</p>
    <h1 class="poster-title">
      <span class="title-main">Moss Petal</span>
      <span class="title-small">and</span>
      <span class="title-small">the</span>
      <span class="title-big">Jumping</span>
      <span class="title-big">Gnomes</span>
    </h1>
    <p class="poster-credits">
      Book by Tod Varga<br>
      Music by Ulric Penhall and Lyrics by Marisol Varga
    </p>
  </main>
</body>
</html>
```